Larkspur Realty

Business cards for 4 people

They need to say for all
57 Danner Quay, Boston MA 02117

Each person will have their own personal information
We would like gold embossing for the name of the company
Mabel is the blonde sitting in the chair smiling her information should be on the back of the card with her name and information
Should say for slogan classic pattern, elevated experience
mabel@larkspurhomesnet.com
(413) 555-0182

Odessa is the brunette with wavy hair in the tan suit odessa@larkspurhomesnet.com
(617) 555-0147

june@larkspurhomesnet.com
(413) 555-0169
standing next to the chair

ruth@larkspurhomesnet.com
(413) 555-0193
close up headshot

```html
<!DOCTYPE html>
<html lang="en">
<head>
<meta charset="utf-8">
<title>Larkspur Realty – Business Card</title>
<link rel="stylesheet" href="https://fonts.googleapis.com/css2?family=Open+Sans:wght@400;600;700&display=swap">
<style>
  :root {
    --stage: #232324;
    --card: #1f2025;
    --card-back: #1c1d21;
    --gold: #d9a95a;
    --gold-light: #e9c27a;
    --gold-dark: #8a6a38;
    --navy: #1d2b4f;
    --ink: #ffffff;
    --emboss: #33343b;
    --photo-light: #cfd0cb;
    --photo-warm: #9a7152;
  }
  * { margin: 0; padding: 0; box-sizing: border-box; }
  html, body { width: 1200px; height: 780px; overflow: hidden; }
  body {
    background: var(--stage);
    font-family: "Open Sans", Arial, sans-serif;
    color: var(--ink);
    position: relative;
  }
  .card {
    position: absolute;
    top: 236px;
    width: 540px;
    height: 309px;
    overflow: hidden;
    box-shadow: 0 18px 40px rgba(0,0,0,.45);
  }
  .card--front { left: 40px; background: var(--card); }
  .card--back { left: 620px; background: var(--card-back); }

  .brand {
    position: absolute;
    display: flex;
    align-items: center;
    gap: 10px;
    font-weight: 600;
    text-transform: uppercase;
    letter-spacing: .08em;
    white-space: nowrap;
  }
  .brand__mark { border-radius: 50%; flex: none; }
  .card--front .brand { left: 150px; top: 26px; font-size: 17px; color: var(--gold); }
  .card--front .brand__mark { width: 38px; height: 38px; border: 2px solid var(--gold); }
  .card--back .brand {
    left: 50%; top: 50%; transform: translate(-50%, -50%);
    font-size: 34px; color: var(--emboss);
    gap: 18px;
  }
  .card--back .brand__mark { width: 90px; height: 90px; border: 3px solid var(--emboss); }

  .name-band {
    position: absolute;
    left: 0; top: 84px;
    width: 340px; height: 40px;
    background: linear-gradient(90deg, var(--gold-light) 0%, var(--gold) 35%, var(--gold-dark) 70%, rgba(31,32,37,0) 100%);
    padding-left: 34px;
    display: flex; align-items: center;
  }
  .name { font-size: 27px; font-weight: 700; letter-spacing: .01em; white-space: nowrap; }
  .title { position: absolute; left: 34px; top: 128px; font-size: 11.5px; }

  .address { position: absolute; left: 34px; top: 156px; font-size: 14px; line-height: 1.35; font-style: normal; }
  .contacts { position: absolute; left: 14px; top: 204px; list-style: none; font-size: 14px; line-height: 1.6; }
  .contacts li { display: flex; align-items: center; gap: 8px; }
  .contacts svg { width: 12px; height: 12px; flex: none; }

  .portrait { position: absolute; left: 0; top: 0; }
</style>
</head>
<body>

<section class="card card--front" aria-label="Business card front">
  <svg class="portrait" width="540" height="309" viewBox="0 0 540 309">
    <defs>
      <linearGradient id="photoTone" x1="0" y1="0" x2="0.6" y2="1">
        <stop offset="0" stop-color="#cfd0cb"/>
        <stop offset="0.55" stop-color="#b8a08a"/>
        <stop offset="1" stop-color="#9a7152"/>
      </linearGradient>
    </defs>
    <circle cx="495" cy="300" r="200" fill="none" stroke="#d9a95a" stroke-width="4"/>
    <circle cx="495" cy="300" r="196" fill="none" stroke="#1d2b4f" stroke-width="4"/>
    <circle cx="495" cy="300" r="194" fill="url(#photoTone)" role="img" aria-label="Portrait photo of the agent in a tan suit"/>
  </svg>

  <div class="brand"><span class="brand__mark"></span>Larkspur Realty</div>

  <div class="name-band"><h1 class="name">Odessa Marlowe</h1></div>
  <p class="title">Real Estate Advisor and Sales Manager</p>

  <address class="address">57 Danner Quay,<br>Boston MA 02117</address>

  <ul class="contacts">
    <li>
      <svg viewBox="0 0 12 12"><path d="M3 1l2 2-1 1.5a6 6 0 0 0 3.5 3.5L9 7l2 2-1.5 2C5 10.5 1.5 7 1 2.5z" fill="#d9a95a"/></svg>
      (617) 555-0147
    </li>
    <li>
      <svg viewBox="0 0 12 12"><circle cx="6" cy="6" r="5" fill="none" stroke="#d9a95a" stroke-width="1.4"/><path d="M1 6h10M6 1c-2.5 3-2.5 7 0 10M6 1c2.5 3 2.5 7 0 10" fill="none" stroke="#d9a95a" stroke-width="1"/></svg>
      www.larkspurhomesnet.com
    </li>
    <li>
      <svg viewBox="0 0 12 12"><rect x="1" y="2.5" width="10" height="7" fill="none" stroke="#d9a95a" stroke-width="1.4"/><path d="M1 2.5l5 4 5-4" fill="none" stroke="#d9a95a" stroke-width="1.2"/></svg>
      odessa@larkspurhomesnet.com
    </li>
  </ul>
</section>

<section class="card card--back" aria-label="Business card back">
  <div class="brand"><span class="brand__mark"></span>Larkspur Realty</div>
</section>

</body>
</html>
```